" Soluçoes de tecnologia focadas em impressao e outsourcing de impressao visando a reduçao de custos de impressao e a melhoria de processos para pequenas, médias e grandes empresas corporativas e governo através de licitações. Atendimento ao público(balcão) com soluções de grafica rápida, impressão de dados variáveis, impressão de provas de consursos Gerenciar e racionalizar os processos de impressao/cópia através de uso inteligente de tecnologia de última geraçao. Contabilizar páginas/cópias impressas, gerenciar suprimentos. Otimizar processos internos para cada departamento e necessidade. Solução de digitalização de documentos. "

```html
<!DOCTYPE html>
<html lang="pt-BR">
<head>
<meta charset="utf-8">
<title>Tintaviva — Soluções em Impressão</title>
<link href="https://fonts.googleapis.com/css2?family=Open+Sans:wght@400;600;700;800&display=swap" rel="stylesheet">
<style>
  :root {
    --page-bg: #e8e8e8;
    --topbar: #161616;
    --red: #e3191f;
    --white: #ffffff;
    --nav-text: #8a8a8a;
    --ink: #222222;
    --hero-shade: rgba(0,0,0,0.35);
  }
  * { margin: 0; padding: 0; box-sizing: border-box; }
  html, body { width: 1200px; height: 1200px; overflow: hidden; }
  body {
    background: var(--page-bg);
    font-family: "Open Sans", sans-serif;
    display: flex; align-items: center; justify-content: center;
  }
  .site { width: 1200px; height: 800px; background: var(--white); display: flex; flex-direction: column; }

  .topbar {
    height: 36px; background: var(--topbar);
    display: flex; align-items: center; justify-content: space-between; padding: 0 40px;
  }
  .topbar-dots { display: flex; gap: 14px; }
  .topbar-dots span { width: 9px; height: 9px; border-radius: 50%; background: var(--red); }
  .topbar-contact { display: flex; align-items: center; gap: 18px; color: var(--white); font-size: 13px; font-weight: 600; }
  .topbar-contact .phone { display: flex; align-items: center; gap: 7px; }

  .header {
    height: 114px; display: flex; align-items: center; justify-content: space-between;
    padding: 0 40px 0 46px; border-bottom: 1px solid #eee;
  }
  .brand { display: flex; align-items: center; gap: 12px; font-weight: 800; font-size: 34px; color: var(--ink); letter-spacing: -0.5px; }
  .brand-mark { width: 30px; height: 30px; background: var(--red); }
  .nav { display: flex; gap: 40px; list-style: none; }
  .nav li { font-size: 16px; color: var(--nav-text); font-weight: 400; }
  .nav .caret { font-size: 10px; margin-left: 4px; }

  .hero { position: relative; flex: 1; overflow: hidden; }
  .hero-media {
    position: absolute; inset: 0;
    background: linear-gradient(105deg, #5a6a80 0%, #8fa0b6 28%, #d8dbe0 50%, #b9c0c8 68%, #3d5d93 100%);
  }
  .hero-media::after {
    content: ""; position: absolute; inset: 0;
    background: linear-gradient(90deg, var(--hero-shade) 0%, rgba(0,0,0,0.1) 55%, rgba(0,0,0,0) 100%);
  }
  .hero-copy { position: absolute; left: 48px; top: 200px; width: 600px; color: var(--white); }
  .hero-title { font-size: 54px; font-weight: 800; line-height: 1.08; text-shadow: 0 2px 6px rgba(0,0,0,0.5); }
  .hero-text { margin-top: 20px; font-size: 18px; font-weight: 700; line-height: 1.45; text-shadow: 0 1px 4px rgba(0,0,0,0.6); }
  .hero-button {
    display: inline-block; margin-top: 40px; background: var(--red); color: var(--white);
    font-size: 20px; font-weight: 700; padding: 14px 46px;
  }
  .slider-controls { position: absolute; right: 90px; bottom: 36px; display: flex; align-items: center; gap: 12px; }
  .slider-dot { width: 12px; height: 12px; border-radius: 50%; border: 2px solid var(--white); }
  .slider-dot.is-active { background: var(--red); border-color: var(--red); }
</style>
</head>
<body>
  <div class="site">
    <div class="topbar">
      <div class="topbar-dots"><span></span><span></span></div>
      <div class="topbar-contact">
        <span class="phone">
          <svg width="14" height="14" viewBox="0 0 24 24"><path fill="#e3191f" d="M6.6 10.8a15 15 0 006.6 6.6l2.2-2.2c.3-.3.7-.4 1-.2 1.1.4 2.3.6 3.6.6.6 0 1 .4 1 1V20c0 .6-.4 1-1 1A17 17 0 013 4c0-.6.4-1 1-1h3.5c.6 0 1 .4 1 1 0 1.3.2 2.5.6 3.6.1.3 0 .7-.2 1z"/></svg>
          (00) 0000-0000
        </span>
        <svg width="13" height="13" viewBox="0 0 24 24"><circle cx="12" cy="8" r="5" fill="#e3191f"/><path d="M3 22c0-5 4-8 9-8s9 3 9 8z" fill="#e3191f"/></svg>
        <svg width="13" height="13" viewBox="0 0 24 24"><circle cx="10" cy="10" r="6" fill="none" stroke="#e3191f" stroke-width="3"/><path d="M15 15l6 6" stroke="#e3191f" stroke-width="3"/></svg>
      </div>
    </div>

    <header class="header">
      <div class="brand"><span class="brand-mark"></span>Tintaviva</div>
      <ul class="nav">
        <li>Home</li>
        <li>Institucional<span class="caret">▼</span></li>
        <li>Produtos<span class="caret">▼</span></li>
        <li>Portfólio</li>
        <li>Contato</li>
      </ul>
    </header>

    <section class="hero">
      <div class="hero-media" role="img" aria-label="Foto de uma impressora de grande formato imprimindo banners coloridos em uma gráfica"></div>
      <div class="hero-copy">
        <h1 class="hero-title">Soluções que<br>IMPRESSIONAM...</h1>
        <p class="hero-text">Lorem Ipsum é simplesmente uma simulação de texto da indústria tipográfica e de impressos, e vem sendo utilizado desde o século XVI, quando um impressor desconhecido...</p>
        <span class="hero-button">Saiba mais</span>
      </div>
      <div class="slider-controls">
        <svg width="14" height="20" viewBox="0 0 14 20"><path d="M11 2L3 10l8 8" fill="none" stroke="#fff" stroke-width="3"/></svg>
        <span class="slider-dot is-active"></span>
        <span class="slider-dot"></span>
        <span class="slider-dot"></span>
        <span class="slider-dot"></span>
        <svg width="14" height="20" viewBox="0 0 14 20"><path d="M3 2l8 8-8 8" fill="none" stroke="#fff" stroke-width="3"/></svg>
      </div>
    </section>
  </div>
</body>
</html>
```